Kestrel Valley Alpine Riders Society needs a business card design

We need a business card design for our newly incorporated KVARS. We are helping the NZ Chinese community, as well as everyone else, to organise ski & snowboarding trips, training, and equipments. The design should be creative, energetic, young and vibrant.

Industry/Entity Type

Social Club

Contact Information for Business Card

Logo; Kestrel Valley Alpine Riders Society; Name: Oliver Brandt; Position: President; Address: 42 Marwick Rd, Epsom, Auckland 1051; Mobile: 020 7826 1957; Email: oliver@kvars-club.example; Web: www.kvars-club.example

Requirements
Must have
• 1, The text "Kestrel Valley Alpine Riders Society" should be put together with the supplied logo file to form a new complete logo combination.
• 2, Final design files should be in Adobe Illustrator format and all text must be editable.
Nice to have
• two or three colours

```html
<!DOCTYPE html>
<html lang="en">
<head>
<meta charset="utf-8">
<title>Kestrel Valley Alpine Riders Society – Business Card</title>
<link href="https://fonts.googleapis.com/css2?family=Open+Sans:ital,wght@0,600;0,700;0,800;1,600;1,700&display=swap" rel="stylesheet">
<style>
  :root {
    --page-bg: #cfe9f5;
    --card-sky-top: #3fb4e6;
    --card-sky-bottom: #5ccbf3;
    --goggle-frame: #33a9de;
    --lens-light: #f4f7f9;
    --lens-dark: #2a6fa3;
    --navy: #1d3f8f;
    --white: #ffffff;
    --faint: rgba(255,255,255,0.18);
  }
  * { margin: 0; padding: 0; box-sizing: border-box; }
  html, body { width: 1200px; height: 800px; overflow: hidden; }
  body {
    background: var(--page-bg);
    font-family: "Open Sans", sans-serif;
    position: relative;
  }
  .card {
    position: absolute;
    top: 284px;
    width: 430px;
    height: 238px;
    background: linear-gradient(180deg, var(--card-sky-top) 0%, var(--card-sky-bottom) 100%);
    overflow: hidden;
  }
  .card--front { left: 110px; }
  .card--back { left: 638px; }

  .goggle-frame {
    position: absolute;
    left: 40px; top: 20px;
    width: 363px; height: 206px;
    border-radius: 70px 70px 110px 110px;
    background: var(--goggle-frame);
  }
  .goggle-lens {
    position: absolute;
    left: 48px; top: 28px;
    width: 347px; height: 190px;
    border-radius: 62px 62px 100px 100px;
    background: linear-gradient(180deg, var(--lens-light) 0%, #e2eaef 30%, #9fb7c9 55%, var(--lens-dark) 78%, var(--lens-dark) 100%);
  }
  .brand-mark {
    position: absolute;
    left: 0; right: 0; top: 64px;
    text-align: center;
    font-weight: 800;
    font-size: 46px;
    letter-spacing: 1px;
    color: var(--navy);
  }

  .holder-name {
    position: absolute;
    left: 56px; top: 40px;
    font-weight: 700;
    font-size: 28px;
    color: var(--white);
  }
  .holder-role {
    position: absolute;
    left: 55px; top: 78px;
    font-weight: 700;
    font-size: 16px;
    color: var(--white);
  }
  .brand-watermark {
    position: absolute;
    left: 36px; top: 88px;
    font-weight: 800;
    font-size: 54px;
    letter-spacing: 2px;
    color: var(--faint);
  }
  .contact-list {
    position: absolute;
    left: 57px; top: 116px;
    list-style: none;
    font-style: italic;
    font-weight: 700;
    font-size: 11px;
    line-height: 17px;
    color: var(--white);
  }
</style>
</head>
<body>
  <section class="card card--front" aria-label="Card front">
    <div class="goggle-frame" role="img" aria-label="Ski goggle illustration frame"></div>
    <div class="goggle-lens" role="img" aria-label="Ski goggle lens with snowy reflection"></div>
    <div class="brand-mark">KVARS</div>
  </section>

  <section class="card card--back" aria-label="Card back">
    <div class="brand-watermark" aria-hidden="true">KVARS</div>
    <h1 class="holder-name">Oliver Brandt</h1>
    <p class="holder-role">President</p>
    <ul class="contact-list">
      <li>42 Marwick Rd, Epsom, Auckland 1051</li>
      <li>020 7826 1957</li>
      <li>oliver@kvars-club.example</li>
      <li>www.kvars-club.example</li>
    </ul>
  </section>
</body>
</html>
```